A Speech Therapy Business needs to update their logo

I need an update to the font and color of my logo to look more appealing. I am looking to open a private practice as a Speech Language Pathologist that caters to adults and children. It needs to be sophisticated and friendly at the same time. I want to keep the silhouette in my logo as is, just update the font and color for "Brightpaths".
Industry/Entity Type
Business
Contact Information for Business Card
I want the business card to have my logo, my name (Dorota Valk, CCC-SLP, TSSLD) and that I am a Bilingual Speech Language Pathologist. Also, include my phone number, (555) 271-8390. Include my website, Brightpathsslp.example, and email address, dorotavalk@brightpathsslp.example
Look and feel
Each slider illustrates characteristics of the customer's brand and the style your logo design should communicate.

```html
<!DOCTYPE html>
<html lang="en">
<head>
<meta charset="utf-8">
<title>Brightpaths – Dorota Valk Business Card</title>
<link href="https://fonts.googleapis.com/css2?family=Spectral:wght@400;600&display=swap" rel="stylesheet">
<style>
  :root {
    --ink-navy: #1b3f8b;
    --paper: #ffffff;
    --sky-light: #86e3fb;
    --sky-mid: #5fb5df;
    --ocean-deep: #1d4c95;
    --ocean-soft: #3d77b6;
    --contact-text: #ffffff;
    --icon-tint: #9fdcf5;
  }
  * { margin: 0; padding: 0; box-sizing: border-box; }
  html, body {
    width: 1200px; height: 686px; overflow: hidden;
    background: var(--paper);
  }
  .business-card {
    position: relative;
    width: 1200px; height: 686px;
    background: var(--paper);
    overflow: hidden;
    font-family: "Spectral", Georgia, serif;
  }
  .wave-backdrop {
    position: absolute; inset: 0;
    width: 1200px; height: 686px;
  }
  .brand-name {
    position: absolute;
    left: 48px; top: 218px;
    font-size: 55px;
    font-weight: 400;
    letter-spacing: 3px;
    color: var(--ink-navy);
    line-height: 1;
  }
  .identity {
    position: absolute;
    right: 57px; top: 300px;
    text-align: right;
    color: var(--ink-navy);
  }
  .identity .person-name {
    font-size: 51px;
    font-weight: 600;
    letter-spacing: 5px;
    line-height: 1.1;
    margin-bottom: 4px;
  }
  .identity .credential {
    font-size: 39px;
    font-weight: 400;
    letter-spacing: 2px;
    line-height: 52px;
  }
  .contact-list {
    position: absolute;
    left: 46px; top: 513px;
    list-style: none;
    color: var(--contact-text);
  }
  .contact-list li {
    display: flex; align-items: center;
    height: 47px;
    font-size: 34px;
    letter-spacing: 1.5px;
  }
  .contact-list svg {
    width: 34px; height: 34px;
    margin-right: 32px;
    fill: var(--icon-tint);
    flex: none;
  }
</style>
</head>
<body>
<div class="business-card">
  <svg class="wave-backdrop" viewBox="0 0 1050 600" preserveAspectRatio="none" aria-hidden="true">
    <defs>
      <linearGradient id="skyWave" x1="0" y1="0" x2="1" y2="0">
        <stop offset="0" stop-color="var(--sky-mid)"/>
        <stop offset="0.6" stop-color="var(--sky-light)"/>
        <stop offset="1" stop-color="var(--sky-light)"/>
      </linearGradient>
      <linearGradient id="oceanWave" x1="0" y1="0" x2="1" y2="1">
        <stop offset="0" stop-color="var(--ocean-deep)"/>
        <stop offset="0.5" stop-color="var(--ocean-soft)"/>
        <stop offset="1" stop-color="var(--ocean-deep)"/>
      </linearGradient>
    </defs>
    <path d="M0,280 C200,270 420,330 620,265 C800,205 960,110 1050,0 L1050,600 L0,600 Z" fill="url(#skyWave)"/>
    <path d="M0,370 C250,340 450,425 650,468 C800,500 950,520 1050,520 L1050,600 L0,600 Z" fill="url(#oceanWave)"/>
  </svg>

  <div class="brand-name">BRIGHTPATHS</div>

  <div class="identity">
    <div class="person-name">DOROTA VALK</div>
    <div class="credential">CCC-SLP, TSSLD</div>
    <div class="credential">Bilingual Speech</div>
    <div class="credential">Language Pathologist</div>
  </div>

  <ul class="contact-list">
    <li>
      <svg viewBox="0 0 24 24" aria-hidden="true"><path d="M6.6 10.8c1.4 2.8 3.8 5.1 6.6 6.6l2.2-2.2c.3-.3.7-.4 1-.2 1.1.4 2.3.6 3.6.6.6 0 1 .4 1 1V20c0 .6-.4 1-1 1C10.6 21 3 13.4 3 4c0-.6.4-1 1-1h3.5c.6 0 1 .4 1 1 0 1.3.2 2.5.6 3.6.1.3 0 .7-.2 1z"/></svg>
      (555) 271-8390
    </li>
    <li>
      <svg viewBox="0 0 24 24" aria-hidden="true"><path d="M12 2a10 10 0 1 0 0 20 10 10 0 0 0 0-20zm-1 17.9A8 8 0 0 1 4.1 11L9 16v1c0 1.1.9 2 2 2zm6.9-2.5c-.3-.8-1-1.4-1.9-1.4h-1v-3c0-.6-.4-1-1-1H8v-2h2c.6 0 1-.4 1-1V7h2c1.1 0 2-.9 2-2v-.4a8 8 0 0 1 2.9 12.8z"/></svg>
      brightpathsslp.example
    </li>
    <li>
      <svg viewBox="0 0 24 24" aria-hidden="true"><path d="M20 4H4c-1.1 0-2 .9-2 2v12c0 1.1.9 2 2 2h16c1.1 0 2-.9 2-2V6c0-1.1-.9-2-2-2zm0 4-8 5-8-5V6l8 5 8-5z"/></svg>
      dorotavalk@brightpathsslp.example
    </li>
  </ul>
</div>
</body>
</html>
```